zenKoi - nutrition bars - logo and packaging*

zenKoi develops stress-relief nutrition bars powered by deep profiling machine learning technology, offering personalized stress management routine.
We produce 3 flavors of nutrition bars. in each flavor, we produce 6 stress relief formulations (3 for day, 3 for night) in 2 strengths.

We need a rebranding of our logo and packaging.

Target Market(s)

Full description of the target audience and their needs and lifestyle is explained in the attached presentation

Logo Text

zenKoi

Font styles to use
Script

Colors

Designer to choose colors to be used in the design.

Requirements
Must have
• logo
• Packaging
• Full description of the deliveries is explained in the attached presentation
Nice to have
• concept for boxes, website

```html
<!DOCTYPE html>
<html lang="en">
<head>
<meta charset="utf-8">
<title>zenKoi – tagline font adjusting</title>
<link href="https://fonts.googleapis.com/css2?family=Quicksand:wght@300;400&family=Lato:wght@400;700&family=Montserrat:wght@500&family=Roboto:wght@400&display=swap" rel="stylesheet">
<style>
:root{
  --ink-blue:#4a5aa8;
  --band-blue:#3f51a3;
  --logo-grey:#7d8a94;
  --text-grey:#6f777d;
  --pattern:#dfe3f1;
  --bg:#ffffff;
}
*{margin:0;padding:0;box-sizing:border-box}
html,body{width:1200px;height:1200px;overflow:hidden;background:var(--bg)}
.board{position:relative;width:1200px;height:1200px}
.heading{position:absolute;width:360px;text-align:center;font-family:"Quicksand",sans-serif;color:var(--ink-blue)}
.heading .title{font-size:50px;letter-spacing:5px;line-height:1;font-weight:400}
.heading .sub{font-size:24px;letter-spacing:2px;line-height:1;margin-top:8px;font-weight:400}
.heading.before{left:17px;top:196px}
.heading.after{left:482px;top:196px}

.pack{position:absolute;width:262px;height:715px}
.pack.before{left:68px;top:280px}
.pack.after{left:530px;top:280px}
.pack .wrapper{position:absolute;inset:0}
.abs{position:absolute}

.logo-name{font-family:"Lato",sans-serif;font-weight:400;color:var(--logo-grey);line-height:1;white-space:nowrap}
.logo-tag{font-family:"Lato",sans-serif;color:var(--text-grey);white-space:nowrap;line-height:1}
.before .logo-name{left:40px;top:108px;font-size:60px}
.before .logo-tag{left:117px;top:163px;font-size:11px;letter-spacing:1px}
.after .logo-name{left:35px;top:88px;font-size:66px}
.after .logo-tag{left:114px;top:149px;font-size:13.5px;letter-spacing:-0.2px}

.pattern{background:linear-gradient(135deg,var(--pattern),#eef0f7);border-radius:4px}
.before .pattern{left:37px;top:210px;width:180px;height:200px}
.after .pattern{left:37px;top:200px;width:180px;height:210px}
.plus{width:34px;height:34px}
.before .plus{left:196px;top:228px}
.after .plus{left:196px;top:218px}

.moon{width:30px;height:30px}
.before .moon{left:113px;top:450px}
.after .moon{left:113px;top:442px}

.band{left:30px;width:202px;height:32px;background:var(--band-blue);color:#fff;font-family:"Lato",sans-serif;font-weight:700;font-size:14.5px;display:flex;align-items:center;justify-content:center;white-space:nowrap}
.before .band{top:485px}
.after .band{top:477px}

.molecules{left:28px;width:206px;text-align:center;font-family:"Montserrat",sans-serif;font-weight:500;font-size:13.5px;color:var(--text-grey);white-space:nowrap}
.before .molecules{top:520px}
.after .molecules{top:513px}

.ingredients-art{width:66px;height:30px;background:linear-gradient(90deg,#e6e7e9,#d0d2d5);border-radius:15px}
.before .ingredients-art{left:96px;top:546px}
.after .ingredients-art{left:96px;top:538px}

.flavour{left:30px;width:202px;text-align:center;font-family:"Montserrat",sans-serif;font-weight:500;font-size:14.5px;letter-spacing:1.6px;color:var(--text-grey)}
.before .flavour{top:582px}
.after .flavour{top:576px}
.weight{left:42px;font-family:"Roboto",sans-serif;font-size:15px;color:var(--text-grey)}
.before .weight{top:609px}
.after .weight{top:603px}

.note{position:absolute;left:795px;top:508px;font-family:"Quicksand",sans-serif;font-weight:400;font-size:24px;line-height:22.5px;letter-spacing:2px;color:var(--ink-blue)}
</style>
</head>
<body>
<div class="board">

  <div class="heading before"><div class="title">BEFORE</div><div class="sub">tagline font adjusting</div></div>
  <div class="heading after"><div class="title">AFTER</div><div class="sub">tagline font adjusting</div></div>

  <div class="pack before">
    <svg class="wrapper" viewBox="0 0 262 715" width="262" height="715">
      <defs>
        <linearGradient id="wrapShadeA" x1="0" x2="1">
          <stop offset="0" stop-color="#d9dadc"/><stop offset=".25" stop-color="#f4f4f5"/><stop offset=".55" stop-color="#fbfbfb"/><stop offset="1" stop-color="#dedfe1"/>
        </linearGradient>
      </defs>
      <path d="M0,6 L262,6 L262,60 C262,92 232,108 232,140 L232,575 C232,610 262,628 262,660 L262,712 L0,712 L0,660 C0,628 30,610 30,575 L30,140 C30,108 0,92 0,60 Z" fill="url(#wrapShadeA)"/>
    </svg>
    <div class="abs logo-name">zenKoi</div>
    <div class="abs logo-tag">Calm Daily Ritual</div>
    <div class="abs pattern" role="img" aria-label="Constellation network line pattern"></div>
    <svg class="abs plus" viewBox="0 0 34 34"><path d="M17 3v28M3 17h28" stroke="#3f51a3" stroke-width="5"/></svg>
    <svg class="abs moon" viewBox="0 0 30 30"><path d="M17 4a11 11 0 1 0 9 17A10 10 0 0 1 17 4z" fill="none" stroke="#7d8a94" stroke-width="2"/><path d="M22 6l1 2 2 1-2 1-1 2-1-2-2-1 2-1z" fill="#7d8a94"/></svg>
    <div class="abs band">Deep Restful Night Blue+</div>
    <div class="abs molecules">Extra Plant Based Molecules</div>
    <div class="abs ingredients-art" role="img" aria-label="Outline drawings of an apple, dates and a walnut"></div>
    <div class="abs flavour">Dates, Apples &amp; Nuts</div>
    <div class="abs weight">30 gr</div>
  </div>

  <div class="pack after">
    <svg class="wrapper" viewBox="0 0 262 715" width="262" height="715">
      <defs>
        <linearGradient id="wrapShadeB" x1="0" x2="1">
          <stop offset="0" stop-color="#d9dadc"/><stop offset=".25" stop-color="#f4f4f5"/><stop offset=".55" stop-color="#fbfbfb"/><stop offset="1" stop-color="#dedfe1"/>
        </linearGradient>
      </defs>
      <path d="M0,6 L262,6 L262,60 C262,92 232,108 232,140 L232,575 C232,610 262,628 262,660 L262,712 L0,712 L0,660 C0,628 30,610 30,575 L30,140 C30,108 0,92 0,60 Z" fill="url(#wrapShadeB)"/>
    </svg>
    <div class="abs logo-name">zenKoi</div>
    <div class="abs logo-tag">Calm Daily Ritual</div>
    <div class="abs pattern" role="img" aria-label="Constellation network line pattern"></div>
    <svg class="abs plus" viewBox="0 0 34 34"><path d="M17 3v28M3 17h28" stroke="#3f51a3" stroke-width="5"/></svg>
    <svg class="abs moon" viewBox="0 0 30 30"><path d="M17 4a11 11 0 1 0 9 17A10 10 0 0 1 17 4z" fill="none" stroke="#7d8a94" stroke-width="2"/><path d="M22 6l1 2 2 1-2 1-1 2-1-2-2-1 2-1z" fill="#7d8a94"/></svg>
    <div class="abs band">Deep Restful Night Blue+</div>
    <div class="abs molecules">Extra Plant Based Molecules</div>
    <div class="abs ingredients-art" role="img" aria-label="Outline drawings of an apple, dates and a walnut"></div>
    <div class="abs flavour">Dates, Apples &amp; Nuts</div>
    <div class="abs weight">30 gr</div>
  </div>

  <p class="note">the right-hand tagline<br>is aligned with the<br>right-hand logo,<br>I reduce the spacing<br>of each letter on the<br>tagline to allow<br>the tagline font size<br>to be larger</p>
</div>
</body>
</html>
```